Renata Quisby

Luxury And Style -

Black - White & Gold

Target Market(s)

Fashion

Industry/Entity Type

Fashion

Requirements
Must have
• High-End
Nice to have
• We will Print on Silk Paper

```html
<!DOCTYPE html>
<html lang="en">
<head>
<meta charset="utf-8">
<title>Renata Quisby — Letterhead</title>
<link href="https://fonts.googleapis.com/css2?family=Prata&family=Montserrat:wght@500&display=swap" rel="stylesheet">
<style>
  :root {
    --gold: #c4a052;
    --ink: #231f20;
    --grey: #a2a3a6;
    --paper: #ffffff;
    --backdrop: #ebe8e3;
  }
  * { margin: 0; padding: 0; box-sizing: border-box; }
  html, body {
    width: 982px;
    height: 1200px;
    overflow: hidden;
    background: var(--backdrop);
  }
  .letterhead {
    position: absolute;
    left: 45px;
    top: 23px;
    width: 892px;
    height: 1154px;
    background: var(--paper);
    box-shadow: 0 2px 10px rgba(0,0,0,0.12);
    overflow: hidden;
  }
  .brand-name {
    position: absolute;
    left: 58px;
    top: 124px;
    color: var(--gold);
    font-family: "Prata", serif;
    font-weight: 400;
    font-size: 24px;
    letter-spacing: 3px;
    line-height: 1;
    white-space: nowrap;
  }
  .contact {
    position: absolute;
    right: 28px;
    top: 48px;
    list-style: none;
  }
  .contact-item {
    display: flex;
    align-items: center;
    justify-content: flex-end;
    height: 34px;
    color: var(--ink);
    font-family: "Prata", serif;
    font-size: 14.5px;
    white-space: nowrap;
  }
  .contact-item.email {
    font-family: "Montserrat", sans-serif;
    font-weight: 500;
    font-size: 13.5px;
  }
  .contact-icon {
    width: 20px;
    height: 22px;
    margin-left: 11px;
    flex: none;
  }
  .footer-band {
    position: absolute;
    left: 0;
    top: 0;
    width: 892px;
    height: 1154px;
  }
  .website {
    position: absolute;
    left: 0;
    width: 1164px;
    top: 1108px;
    text-align: center;
    color: var(--paper);
    font-family: "Prata", serif;
    font-size: 18px;
    letter-spacing: 2.6px;
    line-height: 1;
  }
</style>
</head>
<body>
<main class="letterhead">
  <svg class="footer-band" viewBox="0 0 1275 1649" preserveAspectRatio="none" aria-hidden="true">
    <path fill="none" stroke="var(--grey)" stroke-width="4" d="M0 1345 C140 1528 440 1548 700 1510"/>
    <path fill="none" stroke="var(--gold)" stroke-width="6" d="M0 1385 C130 1558 430 1578 700 1538 C960 1502 1160 1518 1275 1622"/>
    <path fill="var(--ink)" d="M0 1420 C120 1585 420 1605 700 1565 C950 1530 1150 1545 1275 1649 L0 1649 Z"/>
  </svg>

  <header>
    <div class="brand-name">RENATA QUISBY</div>

    <ul class="contact">
      <li class="contact-item">214 W Harlow Avenue IL 60002
        <svg class="contact-icon" viewBox="0 0 20 22" fill="none" stroke="var(--gold)" stroke-width="1.1" aria-hidden="true">
          <path d="M10 17 C6 12 4 9.5 4 7 A6 6 0 0 1 16 7 C16 9.5 14 12 10 17 Z"/>
          <circle cx="10" cy="7" r="2.3"/>
          <ellipse cx="10" cy="18.5" rx="6" ry="2"/>
        </svg>
      </li>
      <li class="contact-item">312.555.0148
        <svg class="contact-icon" viewBox="0 0 20 22" fill="none" stroke="var(--gold)" stroke-width="1.1" aria-hidden="true">
          <path d="M4 4 L7 3 L9 8 L7 9.5 C8 12.5 10 14.5 12.5 15.5 L14 13.5 L19 15.5 L18 18.5 C10 19 3 12 4 4 Z"/>
          <path d="M12 5 A5 5 0 0 1 16 9"/>
          <path d="M12 1.5 A8.5 8.5 0 0 1 19.5 9"/>
        </svg>
      </li>
      <li class="contact-item email">hello@renataquisby.com
        <svg class="contact-icon" viewBox="0 0 20 22" fill="none" stroke="var(--gold)" stroke-width="1.1" aria-hidden="true">
          <path d="M1 9 L10 3 L19 9 V20 H1 Z"/>
          <path d="M1 9 L10 15 L19 9"/>
          <path d="M1 20 L8 14 M19 20 L12 14"/>
          <circle cx="10" cy="8.5" r="2.5"/>
        </svg>
      </li>
    </ul>
  </header>

  <footer class="website">www.renataquisby.com</footer>
</main>
</body>
</html>
```